Graphic for playing Card

I need a graphic illustration for a playing card game.
The name of the game is called 'Kites' and that should be incorporated in the design.
I will attach a basic draft of what I want, the rest is a blank canvas. Where you can be as creative as you want.
I like how older playing cards look.
The attached images are just an example of what I want, not necessarily the artwork style. You can be creative thats up to you.
See Nice to haves - you don't have to follow this but if someone would design really nicely like this, they would win for sure.
Rounded corners for the cards
Requirements
Must have
- Card Shape Ratio
- Width = 1
- Height = 1.4
- Text "Kites" as main focus
- Playing Card Theme
Nice to have
- This is optional and would be interesting to see. The card game is from Trinidad and Tobago in the caribbean. If there is somewhere you can be creative using the following things found in Trinidad and Tobago.
- Oil and gas - Drilling Rigs
- Steel Drum - musical instrument
- Scarlet Ibis - red flamingo bird
- chaconia - a red plant (google for idea)
- Carnival - google trinidad carnival
- Additionally the Colors of Trinidad and Tobago or Red, White and Black
Should not have
- Do not look similar to poker or black jack.

```html
<!DOCTYPE html>
<html lang="en">
<head>
<meta charset="UTF-8">
<title>Kites – Playing Card Back</title>
<link rel="stylesheet" href="https://fonts.googleapis.com/css2?family=Lobster&display=swap">
<style>
  :root {
    --backdrop-light: #e4e4e4;
    --backdrop-dark: #b9b9b9;
    --card-border: #ffffff;
    --card-black: #0d0d0d;
    --pattern-light: #6b6b6b;
    --pattern-dark: #1c1c1c;
    --ornament-red: #d0121b;
    --ornament-deep: #7a0a0e;
    --title-white: #ffffff;
    --title-shadow: #c4141c;
  }

  html, body {
    margin: 0;
    padding: 0;
    overflow: hidden;
  }

  .canvas {
    position: relative;
    width: 1200px;
    height: 960px;
    overflow: hidden;
    background: radial-gradient(ellipse at 40% 35%, var(--backdrop-light) 0%, var(--backdrop-dark) 100%);
  }

  .card {
    position: absolute;
    left: 300px;
    top: 60px;
    width: 600px;
    height: 840px;
    box-sizing: border-box;
    padding: 16px;
    border-radius: 48px;
    background: var(--card-border);
    box-shadow: 6px 8px 14px rgba(0, 0, 0, 0.35);
  }

  .card-face {
    position: relative;
    width: 100%;
    height: 100%;
    border-radius: 36px;
    overflow: hidden;
    background: var(--card-black);
  }

  .pattern-field {
    position: absolute;
    left: 0;
    width: 100%;
    height: 100%;
    background: radial-gradient(ellipse at 50% 50%, var(--pattern-light) 0%, var(--pattern-dark) 85%);
  }

  .title-band {
    position: absolute;
    left: 0;
    top: 262px;
    width: 100%;
    height: 300px;
    background: var(--card-black);
    box-shadow: 0 0 30px 10px rgba(0, 0, 0, 0.7);
  }

  .ornament {
    position: absolute;
    left: 14%;
    width: 72%;
    height: 60px;
    border-radius: 50%;
    background: linear-gradient(90deg, var(--ornament-deep) 0%, var(--ornament-red) 50%, var(--ornament-deep) 100%);
  }

  .ornament--top { top: 20px; }
  .ornament--bottom { bottom: 20px; }

  .game-title {
    position: absolute;
    left: 0;
    top: 50%;
    width: 100%;
    margin: 0;
    transform: translateY(-50%);
    text-align: center;
    font-family: "Lobster", cursive;
    font-weight: 400;
    font-size: 150px;
    line-height: 1;
    color: var(--title-white);
    text-shadow: 5px 5px 0 var(--title-shadow);
  }
</style>
</head>
<body>
  <main class="canvas">
    <section class="card" aria-label="Kites playing card back">
      <div class="card-face">
        <div class="pattern-field" role="img" aria-label="Silver swirling filigree pattern fading into black"></div>
        <div class="title-band">
          <div class="ornament ornament--top" role="img" aria-label="Red tribal flourish ornament"></div>
          <h1 class="game-title">Kites</h1>
          <div class="ornament ornament--bottom" role="img" aria-label="Red tribal flourish ornament"></div>
        </div>
      </div>
    </section>
  </main>
</body>
</html>
```